Website Comps for Famous Southern BBQ Restaurant in Alabama

We need an authentic, brand-focused redesign for a restaurant.

We need an authentic look.
The client really likes this website.
https://pelzerpit.com/

I don't want to see a bunch of crazy colors.
Avoid image sliders on the homepage. I hate those.

Please mockup the following three pages:
Homepage
Interior page (for mockup purposes, you can do an About page)
Menu page

I only need the PSD's; not the website coded.

Here is the current website: www.dunmoresmokehouse.com

https://pelzerpit.com/

Here are some additional stock photos. New photos will be shot, but these may help for your mock-up designs.
https://www.filecrate.net/sh/83kqvtrpe21zwa9/QXM71bTr4-plWnfVoe8KtYjd?dl=0
Updates

I realize we don't have a lot of high-quality photos to work with.Those will be shot.Here are some additional stock photos that may help.https://www.filecrate.net/sh/83kqvtrpe21zwa9/QXM71bTr4-plWnfVoe8KtYjd?dl=0 Added Saturday, June 10, 2017

Target Market(s)

United states

Industry/Entity Type

Restaurant

Number of Pages Required

3 page

Font styles to use
Sans Serif

Colors

Designer to choose colors to be used in the design.

Requirements
Must have
• An authentic look.
• The client really likes this website.
• https://pelzerpit.com/
• It's simple, bold, and vintage at the same time.
• That is what we want.
• Our existing website is
• dunmoresmokehouse.com
Nice to have
• Simplicity. Something that makes the food look good.
• Possibly a background.
• Logo:
• https://www.filecrate.net/s/k58tnwpl3ovza2e/dunmore-smokehouse-ridgeway.png?dl=0
• Here is a sampling of photos for your comps:
• https://www.filecrate.net/sh/61vbqzhoewpxtn4/QLT4b8JKyRmPPwf6c2ZnHUVpe?dl=0
Should not have
• Nothing too busy.
• Not too many colors.
• Keep it simple, authentic, "down home."
• No homepage image sliders.

```html
<!DOCTYPE html>
<html lang="en">
<head>
<meta charset="utf-8">
<title>Dunmore Smokehouse — Home</title>
<link href="https://fonts.googleapis.com/css2?family=Passion+One:wght@400;700&family=Exo+2:wght@400;600;700&family=Lobster+Two:ital,wght@1,700&display=swap" rel="stylesheet">
<style>
:root{
  --maroon:#5a1a0c;
  --red:#b8251c;
  --red-dark:#7d160f;
  --cream:#f3e9dc;
  --card:#efe4d3;
  --orange:#f5a623;
  --gold:#f3b12b;
  --ink:#3a2a20;
  --grey:#6b6157;
  --footer:#3b2418;
}
*{margin:0;padding:0;box-sizing:border-box}
html,body{width:1200px;height:2490px;overflow:hidden}
body{position:relative;background:var(--cream);font-family:"Exo 2",sans-serif;color:var(--ink)}
.abs{position:absolute}
.display{font-family:"Passion One",sans-serif;text-transform:uppercase;letter-spacing:1px;line-height:.95}
.script{font-family:"Lobster Two",cursive;font-style:italic;font-weight:700}
.site-header{left:0;top:0;width:1200px;height:106px;background:linear-gradient(#d9dfe0,#b9c3c6)}
.brand{left:113px;top:8px;width:82px;height:82px;background:var(--red-dark);border:2px solid #2b0a05;display:flex;align-items:center;justify-content:center;text-align:center;color:var(--gold);font-family:"Passion One",sans-serif;font-size:17px;line-height:1.05;text-transform:uppercase}
.main-nav{left:302px;top:27px;width:788px;height:46px;background:var(--red);border:3px solid var(--red-dark);border-radius:6px;box-shadow:0 0 0 2px #e05a4a inset;display:flex;justify-content:space-around;align-items:center;padding:0 14px}
.main-nav a{color:#fff;text-decoration:none;font-weight:700;font-size:14px;text-transform:uppercase}
.rule-band{left:0;top:106px;width:1200px;height:26px;background:repeating-linear-gradient(#e6e3dc 0 3px,#c7c2b8 3px 5px)}
.hero{left:0;top:132px;width:1200px;height:1174px;background:radial-gradient(ellipse at 60% 45%,#8a7a70 0%,#4a3a33 40%,#241812 80%)}
.card{background:var(--card);border-radius:12px;box-shadow:0 4px 12px rgba(0,0,0,.45)}
.photo{background:linear-gradient(135deg,#8e6d55,#4c3a2e)}
.card-title{color:var(--maroon);text-align:center}
.story-text{font-size:13.5px;line-height:1.75;text-align:center;color:var(--ink)}
.read-more{color:var(--ink);font-size:19px}
.tag-more{background:var(--maroon);color:var(--cream);font-size:17px;text-align:center;border-radius:0 0 10px 10px;padding:3px 0}
.info{text-align:center;color:var(--grey);font-size:13px;line-height:1.3}
.info .lbl{font-family:"Passion One",sans-serif;text-transform:uppercase;color:var(--maroon);font-size:18px;line-height:.95;display:block}
.info .dir{font-family:"Lobster Two",cursive;font-style:italic;font-weight:700;font-size:18px;color:var(--ink)}
.accolade{left:613px;top:160px;width:477px;height:195px;border:2px solid var(--cream);outline:1px solid var(--cream);outline-offset:-8px;border-radius:6px;display:flex;align-items:center;justify-content:center;text-align:center;color:var(--gold);font-size:36px}
.promo{background:var(--orange);border:3px solid var(--cream);border-radius:14px;box-shadow:0 4px 12px rgba(0,0,0,.5)}
.promo .display{color:var(--maroon)}
.section-title{color:var(--maroon);text-align:center;font-size:33px}
.notice{left:118px;width:460px;height:84px;background:#fff;display:flex;align-items:center;gap:14px;padding-left:12px}
.date-dot{width:66px;height:66px;border-radius:50%;background:var(--maroon);color:var(--cream);display:flex;flex-direction:column;align-items:center;justify-content:center;font-weight:600;font-size:15px;line-height:1.05}
.date-dot b{color:var(--gold);font-weight:700}
.notice p{font-size:18px;font-weight:600;color:#4a3a30;text-transform:uppercase}
.news-item{left:613px;width:477px;height:110px;background:#fff;border:1px solid #e2d8cc;display:flex;gap:18px;padding:4px}
.news-item .thumb{width:162px;height:100px;flex:none}
.news-item h3{font-size:14px;font-weight:700;line-height:1.35;margin-top:10px;color:#2a1f18}
.news-item small{display:block;font-size:11.5px;color:var(--grey);margin-top:4px;line-height:1.4}
.pits{left:0;top:1900px;width:1200px;height:375px;background:radial-gradient(ellipse at 62% 70%,#a0581d 0%,#3a2418 35%,#120b08 80%)}
.pits-title{left:0;width:1200px;text-align:center;color:#fff;line-height:1}
.ribbon{background:var(--orange);color:var(--maroon);font-weight:700;font-size:15px;padding:3px 14px}
.btn{background:var(--orange);color:var(--maroon);border-radius:4px;font-size:22px;padding:3px 26px}
.site-footer{left:0;top:2275px;width:1200px;height:215px;background:var(--footer);border-top:6px solid #c9bca9}
.site-footer h4{color:#fff;font-size:14px;font-weight:700;text-transform:uppercase}
.site-footer a{color:#d9ccbd;font-size:13px;text-decoration:none;display:block;line-height:22px}
.social span{display:inline-block;width:27px;height:27px;border-radius:50%;background:#9b8f84;margin-right:7px}
</style>
</head>
<body>

<header class="abs site-header">
  <div class="abs brand">Dunmore<br>Smoke<br>house</div>
  <nav class="abs main-nav">
    <a href="#">Home</a><a href="#">About</a><a href="#">Locations</a><a href="#">Restaurant Menus</a><a href="#">Catering</a><a href="#">News</a><a href="#">Store</a><a href="#">Contact Us</a>
  </nav>
</header>
<div class="abs rule-band"></div>

<section class="abs hero" role="img" aria-label="Smoky barbecue grill with meat over the coals"></section>

<article class="abs card" style="left:110px;top:183px;width:477px;height:485px">
  <div class="abs photo" style="left:5px;top:5px;width:467px;height:240px;border-radius:10px 10px 0 0" role="img" aria-label="Owner seated in a diner booth under vintage tin signs"></div>
  <div class="abs" style="left:206px;top:232px;width:66px;height:30px;border-radius:50%;background:var(--maroon)"></div>
  <h2 class="abs display card-title" style="left:0;top:272px;width:477px;font-size:36px">Dunmore's Story</h2>
  <p class="abs story-text" style="left:38px;top:322px;width:400px">For Dale Dunmore, growing up in North Carolina meant a whole lot of good times BS'ing and backyard barbecuing with friends. In high school, Dale earned himself a nickname, for assorted reasons that may not be revealed</p>
  <div class="abs script read-more" style="left:0;top:432px;width:477px;text-align:center">Read More</div>
</article>

<div class="abs display accolade">No. 1<br>on Marla Quinn's list<br>of 10 best barbecue<br>places in America</div>

<article class="abs card" style="left:613px;top:380px;width:477px;height:288px">
  <h2 class="abs display card-title" style="left:0;top:12px;width:477px;font-size:34px">Dunmore Smokehouse,<br><span style="font-size:24px">Ridgeway</span></h2>
  <div class="abs photo" style="left:158px;top:88px;width:160px;height:175px" role="img" aria-label="Red vintage cola and ice sign on a storefront"></div>
  <div class="abs tag-more script" style="left:158px;top:262px;width:160px">Read More</div>
  <div class="abs info" style="left:10px;top:70px;width:140px"><svg width="30" height="38" viewBox="0 0 30 38"><path d="M15 2a11 11 0 0 1 11 11c0 9-11 22-11 22S4 22 4 13A11 11 0 0 1 15 2z" fill="none" stroke="#6b6157" stroke-width="2"/><circle cx="15" cy="13" r="4" fill="none" stroke="#6b6157" stroke-width="2"/></svg><span class="lbl">Our<br>Location</span>1412 Tanner Road<br>Ridgeway AL<br>35790<br><span class="dir">Get Directions</span></div>
  <div class="abs info" style="left:326px;top:70px;width:145px"><svg width="38" height="38" viewBox="0 0 38 38"><circle cx="19" cy="19" r="16" fill="none" stroke="#6b6157" stroke-width="2"/><path d="M19 9v10l7 4" fill="none" stroke="#6b6157" stroke-width="2"/></svg><span class="lbl">Our<br>Hours</span>Mon - Sat:<br><b style="font-size:15px">11 AM - 8 PM</b><span class="lbl" style="margin-top:12px">Phone</span>(555) 214-0387</div>
</article>

<article class="abs card" style="left:110px;top:688px;width:477px;height:288px">
  <h2 class="abs display card-title" style="left:0;top:12px;width:477px;font-size:34px">Dunmore's Juke Joint,<br><span style="font-size:24px">Birchfield</span></h2>
  <div class="abs photo" style="left:158px;top:88px;width:160px;height:175px" role="img" aria-label="Bar interior with hanging flag"></div>
  <div class="abs tag-more script" style="left:158px;top:262px;width:160px">Read More</div>
  <div class="abs info" style="left:10px;top:70px;width:140px"><svg width="30" height="38" viewBox="0 0 30 38"><path d="M15 2a11 11 0 0 1 11 11c0 9-11 22-11 22S4 22 4 13A11 11 0 0 1 15 2z" fill="none" stroke="#6b6157" stroke-width="2"/><circle cx="15" cy="13" r="4" fill="none" stroke="#6b6157" stroke-width="2"/></svg><span class="lbl">Our<br>Location</span>318 Pell Ave.<br>Calloway, AL<br>35712<br><span class="dir">Get Directions</span></div>
  <div class="abs info" style="left:326px;top:70px;width:145px"><svg width="38" height="38" viewBox="0 0 38 38"><circle cx="19" cy="19" r="16" fill="none" stroke="#6b6157" stroke-width="2"/><path d="M19 9v10l7 4" fill="none" stroke="#6b6157" stroke-width="2"/></svg><span class="lbl">Our<br>Hours</span>Mon - Sat:<br><b style="font-size:15px">11:00 am - 12:00 am/midnight</b><span class="lbl" style="margin-top:6px">Phone</span>(555) 214-0387</div>
</article>

<article class="abs card" style="left:613px;top:688px;width:477px;height:288px">
  <h2 class="abs display card-title" style="left:0;top:12px;width:477px;font-size:34px">Dunmore's Soul Kitchen,<br><span style="font-size:24px">Elmwood</span></h2>
  <div class="abs" style="left:158px;top:88px;width:160px;height:175px;background:linear-gradient(#4a86c9,#a8c8e6)" role="img" aria-label="Round restaurant sign on a pole against blue sky"></div>
  <div class="abs tag-more script" style="left:158px;top:262px;width:160px">Read More</div>
  <div class="abs info" style="left:10px;top:70px;width:140px"><svg width="30" height="38" viewBox="0 0 30 38"><path d="M15 2a11 11 0 0 1 11 11c0 9-11 22-11 22S4 22 4 13A11 11 0 0 1 15 2z" fill="none" stroke="#6b6157" stroke-width="2"/><circle cx="15" cy="13" r="4" fill="none" stroke="#6b6157" stroke-width="2"/></svg><span class="lbl">Our<br>Location</span>207 Hollis St.<br>Calloway, AL<br>35718<br><span class="dir">Get Directions</span></div>
  <div class="abs info" style="left:326px;top:70px;width:145px"><svg width="38" height="38" viewBox="0 0 38 38"><circle cx="19" cy="19" r="16" fill="none" stroke="#6b6157" stroke-width="2"/><path d="M19 9v10l7 4" fill="none" stroke="#6b6157" stroke-width="2"/></svg><span class="lbl">Our<br>Hours</span>Mon - Sat:<br><b style="font-size:14px">11:00 am - 8 pm<br>Sun: 11:00 am - 4</b><span class="lbl" style="margin-top:6px">Phone</span>(555) 214-0962</div>
</article>

<div class="abs promo" style="left:110px;top:1045px;width:477px;height:220px">
  <h2 class="abs display" style="left:30px;top:35px;font-size:40px">Our Store</h2>
  <p class="abs" style="left:30px;top:78px;color:#fff;font-weight:700;font-size:14px;text-transform:uppercase;line-height:1.2">Welcome to Dunmore's<br>online store!</p>
  <div class="abs script" style="left:30px;top:155px;font-size:20px;color:var(--maroon)">View More Products</div>
  <div class="abs" style="left:345px;top:22px;width:56px;height:180px;border-radius:18px 18px 6px 6px;background:linear-gradient(#6b2a10,#b24a16)" role="img" aria-label="Bottle of barbecue sauce"></div>
</div>
<div class="abs promo" style="left:613px;top:1045px;width:477px;height:220px;text-align:center">
  <svg class="abs" style="left:205px;top:14px" width="66" height="64" viewBox="0 0 66 64"><path d="M6 8h24l3 4 3-4h24v50H36l-3 4-3-4H6z" fill="none" stroke="#5a1a0c" stroke-width="2.5"/><path d="M33 12v46M14 22h12M14 30h12M40 22h12M40 30h12M40 38h12" stroke="#5a1a0c" stroke-width="2"/></svg>
  <h2 class="abs display" style="left:0;top:96px;width:477px;font-size:40px">Restaurant<br>Menus</h2>
  <div class="abs script" style="left:0;top:178px;width:477px;font-size:20px;color:var(--maroon)">View Restaurant Menus</div>
</div>

<h2 class="abs display section-title" style="left:118px;top:1357px;width:460px">We have very important<br>anouncements</h2>
<div class="abs notice" style="top:1452px"><div class="date-dot">JUL<b>04</b></div><p>Closed for Independence Day</p></div>
<div class="abs notice" style="top:1544px"><div class="date-dot">JUL<b>01-10</b></div><p>Closed for our annual vacation</p></div>
<div class="abs notice" style="top:1636px"><div class="date-dot">JUL<b>05</b></div><p>Closed for Lone Star Quarterly BBQ</p></div>
<div class="abs notice" style="top:1728px"><div class="date-dot">JUL<b>23-24</b></div><p>Closed for Thanksgiving</p></div>

<h2 class="abs display section-title" style="left:613px;top:1357px;width:477px">Latest<br>news/events</h2>
<div class="abs news-item" style="top:1452px"><div class="thumb photo" role="img" aria-label="Pork-stuffed baked potato"></div><div><h3>Pork-Stuffed Tater is on the Menu in "Fifty Plates Worth the Drive in Dixie"</h3><small>By dunmore | On March 9, 2016 | in News with Comments Off</small></div></div>
<div class="abs news-item" style="top:1573px"><div class="thumb photo" role="img" aria-label="Barbecue sandwich with baked beans"></div><div><h3>Trail &amp; Table Magazine Proclaims Dunmore's "Best Barbecue in America"</h3><small>By dunmore | On March 9, 2016 | in News with Comments Off</small></div></div>
<div class="abs news-item" style="top:1694px"><div class="thumb photo" role="img" aria-label="Burger with lettuce and tomato"></div><div><h3>Porch &amp; Pasture Names Dunmore Smokehouse One of the South's Best Burger Joints</h3><small>By dunmore | On December 17, 2014 | in News with Comments Off</small></div></div>
<div class="abs script" style="left:613px;top:1815px;width:477px;text-align:center;font-size:21px">View More</div>

<section class="abs pits" role="img" aria-label="Pitmaster welding a barbecue smoker in a workshop"></section>
<div class="abs ribbon" style="left:528px;top:2003px">COMING IN 2018</div>
<h2 class="abs display pits-title" style="top:2034px;font-size:66px">Dunmore's</h2>
<div class="abs display pits-title" style="top:2099px;font-size:44px;letter-spacing:2px">Barbecue Pits</div>
<div class="abs script btn" style="left:530px;top:2158px">Get info!</div>

<footer class="abs site-footer">
  <div class="abs brand" style="left:110px;top:28px;width:102px;height:102px;font-size:20px">Dunmore<br>Smoke<br>house</div>
  <h4 class="abs" style="left:240px;top:35px">Quick Links</h4>
  <div class="abs" style="left:240px;top:58px"><a href="#">Home</a><a href="#">About</a><a href="#">Locations</a><a href="#">Restaurant Menus</a></div>
  <div class="abs" style="left:380px;top:58px"><a href="#">Catering</a><a href="#">News</a><a href="#">Store</a><a href="#">Contact Us</a></div>
  <h4 class="abs" style="left:485px;top:35px">We're Social</h4>
  <div class="abs social" style="left:485px;top:64px"><span></span><span></span><span></span><span></span></div>
  <div class="abs script" style="left:720px;top:28px;color:#fff;font-size:21px">Newsletter</div>
  <div class="abs" style="left:720px;top:68px;width:228px;border-bottom:1px solid #cbbfae;color:#cbbfae;font-size:13px;padding-bottom:8px">Enter your email</div>
  <div class="abs script btn" style="left:965px;top:62px;font-size:20px;padding:3px 24px">Sign Up!</div>
  <div class="abs" style="left:0;top:147px;width:1200px;border-top:1px solid #5a3e30"></div>
  <p class="abs" style="left:110px;top:170px;color:#bfb2a3;font-size:12px">© 2017 Dunmore Smokehouse</p>
</footer>

</body>
</html>
```